Business Card Design

Cake decorating business in a small town in Australia. looking for a style that is fresh with a touch of vintage/country. liking these ideas, timber backgrounds, chalkboards, bunting, flowers and cake elements (rolling pins, cupcakes, cake stands, etc.) would consider a shot saying/statement. would like the back of the card to have wording "Specialising in delectable treats for all your special occasions" - wedding cakes - birthday cakes - special occasion cakes - novelty cakes - cupcakes, cookies, slices and cake pops. maybe incorporate a cake in design on back page. attached are a few of my favourite cakes and the start of a card design I liked.

Industry/Entity Type

Business

Contact Information for Business Card

Marigold's Sugarloft Bakes 0438 056 969Find me on (Chirpwall Logo)

Requirements
Nice to have
• timber, some of my designs, chalkboard, baking utensils
Should not have
• no red font

```html
<!DOCTYPE html>
<html lang="en">
<head>
<meta charset="utf-8">
<title>Marigold's Sugarloft Bakes – Business Cards</title>
<link href="https://fonts.googleapis.com/css2?family=Lobster&family=Open+Sans:wght@400;600&display=swap" rel="stylesheet">
<style>
  :root {
    --canvas: #e9e6e2;
    --card-white: #ffffff;
    --card-black: #050505;
    --ink: #2a2a2a;
    --text-light: #f4f4f4;
    --brand-pink: #e9a3b8;
    --photo-1a: #b9b9b9; --photo-1b: #5e5e5e;
    --photo-2a: #e4e4e4; --photo-2b: #9a9a9a;
    --photo-3a: #cfcfcf; --photo-3b: #7b7b7b;
    --photo-4a: #a8a8a8; --photo-4b: #3f3f3f;
    --photo-5a: #ececec; --photo-5b: #b0b0b0;
  }
  * { box-sizing: border-box; margin: 0; padding: 0; }
  html, body { width: 1200px; height: 900px; overflow: hidden; }
  body {
    background: var(--canvas);
    font-family: "Open Sans", Arial, sans-serif;
    position: relative;
  }
  .card {
    position: absolute;
    left: 280px;
    width: 640px;
    height: 366px;
    background: var(--card-black);
    overflow: hidden;
    box-shadow: 0 6px 18px rgba(0,0,0,0.18);
  }
  .card--back { top: 40px; }
  .card--front { top: 470px; }

  .card__white-band {
    position: absolute; left: 0; top: 0; width: 100%;
    background: var(--card-white);
  }
  .card--back .card__white-band { height: 160px; }
  .card--front .card__white-band { height: 150px; }

  /* Back */
  .back__name {
    position: absolute; left: 0; right: 0; top: 98px;
    text-align: center;
    font-family: "Lobster", cursive;
    font-size: 32px;
    line-height: 1;
    white-space: nowrap;
    color: var(--ink);
  }
  .back__tagline {
    position: absolute; left: 0; right: 0; top: 196px;
    text-align: center;
    color: var(--text-light);
    font-size: 11px;
    letter-spacing: 0.6px;
    line-height: 1.4;
    text-transform: uppercase;
  }

  /* Front */
  .front__brand {
    position: absolute; left: 0; right: 0; top: 28px;
    display: flex; justify-content: center; align-items: center; gap: 14px;
  }
  .front__brand-mark {
    width: 54px; height: 54px;
    background: var(--brand-pink);
    flex: none;
  }
  .front__name {
    font-family: "Lobster", cursive;
    font-size: 34px;
    line-height: 1;
    white-space: nowrap;
    color: var(--ink);
  }
  .front__photo-strip {
    position: absolute; left: 58px; top: 100px;
    width: 524px; height: 116px;
    display: flex;
  }
  .front__photo { flex: 1; }
  .front__photo--hat     { background: linear-gradient(165deg, var(--photo-1a), var(--photo-1b)); }
  .front__photo--flowers { background: linear-gradient(180deg, var(--photo-2b), var(--photo-2a)); }
  .front__photo--gift    { background: linear-gradient(150deg, var(--photo-3b), var(--photo-3a)); }
  .front__photo--camera  { background: linear-gradient(190deg, var(--photo-4a), var(--photo-4b)); }
  .front__photo--initials{ background: linear-gradient(170deg, var(--photo-5b), var(--photo-5a)); }

  .front__contact {
    position: absolute; left: 82px;
    display: flex; align-items: center; gap: 12px;
    color: var(--text-light);
    font-size: 21px;
    line-height: 1;
    letter-spacing: 0.8px;
    white-space: nowrap;
  }
  .front__contact--phone { top: 256px; }
  .front__contact--social { top: 300px; }
  .icon { width: 18px; height: 18px; flex: none; }
  .icon--square { background: var(--text-light); border-radius: 2px; width: 16px; height: 16px; }
</style>
</head>
<body>

  <section class="card card--back" aria-label="Card back">
    <div class="card__white-band"></div>
    <p class="back__name">Marigold's Sugarloft Bakes</p>
    <p class="back__tagline">"Specialising in delectable treats<br>for all your special occasions"</p>
  </section>

  <section class="card card--front" aria-label="Card front">
    <div class="card__white-band"></div>
    <div class="front__brand">
      <span class="front__brand-mark" aria-hidden="true"></span>
      <p class="front__name">Marigold's Sugarloft Bakes</p>
    </div>
    <div class="front__photo-strip">
      <div class="front__photo front__photo--hat" role="img" aria-label="Photo of a cowboy hat birthday cake"></div>
      <div class="front__photo front__photo--flowers" role="img" aria-label="Photo of a white cake with sugar flowers"></div>
      <div class="front__photo front__photo--gift" role="img" aria-label="Photo of a gift box cake with bow"></div>
      <div class="front__photo front__photo--camera" role="img" aria-label="Photo of a camera novelty cake"></div>
      <div class="front__photo front__photo--initials" role="img" aria-label="Photo of an engagement cake with initials"></div>
    </div>
    <p class="front__contact front__contact--phone">
      <svg class="icon" viewBox="0 0 24 24" aria-hidden="true">
        <path fill="#f4f4f4" d="M3 9c0-3 4-5 9-5s9 2 9 5v2h-5V9c-1-1-7-1-8 0v2H3zM6 12h12l2 8H4z"/>
        <circle cx="12" cy="16" r="2" fill="#050505"/>
      </svg>
      <span>0417 382 254</span>
    </p>
    <p class="front__contact front__contact--social">
      <span class="icon icon--square" aria-hidden="true"></span>
      <span>/marigoldssugarloftbakes</span>
    </p>
  </section>

</body>
</html>
```